Dog Snacks brand needs a new packaging design

Dear Designers,

We are looking for a packaging expert to design our new line of Dog Snacks which contain a relaxing hemp extract (CBD).

Our company is already selling various relaxing cat & dog products , and we would like this new design to reflect the same "style & feeling" as our current products (see attached instructions).

Technical aspects:
- The packaging is a Stand Up Pouch (12x18.5x7cm - see attached instructions).
- Please follow technical guidelines from printer (see attached instructions).
- The packaging will contain 120g of high-quality, semi-moist dog snacks.
- We will be designing 3 differents variations for 3 different flavours: Chicken, Beef & Liver.
- The packaging will be printed with a matt finish.

Design aspects:
- The design should be compatible with our brand identity (i.e. fluffly, pure, relaxing, positive, clean & natural).
- Soft/rounded shapes are preferred.
- Please use our brand's colors (#3BA384, White & Black).
- Please use our company logo (see attached instructions).
- The design also needs to convey a strong sense of professionalism as we are an animal "healthcare" brand.
- If you want to include a dog picture, we would prefer you to use a picture of our official brand ambassador (see attached instructions).
- We have attached a number of packaging examples which we like a lot. (see attached instructions). Please only use those as general inspiration.
- Only original work (no plagiarism will be accepted).

Please don't hesitate to send us a message if you have any questions about the brand, the product or the design requirements.

We look forward to seeing your designs & working on this together !

Thanks & regards,
Marcus

Dog owners

Pet Care

Sans Serif

• Please see project description.

```html
<!DOCTYPE html>
<html lang="en">
<head>
<meta charset="utf-8">
<title>Verdalia CBD Treats – Pouch Front</title>
<link rel="stylesheet" href="https://fonts.googleapis.com/css2?family=Courier+Prime:wght@400;700&family=Raleway:wght@300;500;600&display=swap">
<style>
  :root {
    --brand-green: #3ba384;
    --deep-green: #23805f;
    --soft-green: #6cbfa5;
    --ink: #111111;
    --paper: #ffffff;
    --backdrop: #c9c9c9;
  }
  * { margin: 0; padding: 0; box-sizing: border-box; }
  html, body {
    width: 1200px;
    height: 835px;
    overflow: hidden;
    background: var(--backdrop);
  }
  .canvas {
    position: relative;
    width: 1200px;
    height: 835px;
  }
  .pouch {
    position: absolute;
    left: 380px;
    top: 32px;
    width: 440px;
    height: 770px;
    background: var(--paper);
    border-radius: 14px 14px 6px 6px;
    overflow: hidden;
  }
  .pouch-top {
    position: absolute;
    left: 0; top: 0;
    width: 440px; height: 60px;
  }
  .line-name {
    position: absolute;
    left: 30px;
    top: 633px;
    transform: rotate(-90deg);
    transform-origin: left top;
    font-family: "Courier Prime", monospace;
    font-size: 46px;
    letter-spacing: 6px;
    color: var(--deep-green);
    white-space: nowrap;
    width: 560px;
    text-align: center;
    line-height: 48px;
  }
  .brand {
    position: absolute;
    left: 110px;
    top: 150px;
    width: 215px;
    text-align: right;
  }
  .brand-row {
    display: flex;
    align-items: center;
    justify-content: flex-end;
    gap: 10px;
  }
  .brand-dot {
    width: 16px; height: 16px;
    border-radius: 50%;
    background: var(--brand-green);
  }
  .brand-name {
    font-family: "Raleway", sans-serif;
    font-weight: 500;
    font-size: 38px;
    color: var(--ink);
    letter-spacing: 0.5px;
  }
  .brand-tag {
    font-family: "Courier Prime", monospace;
    font-size: 16px;
    color: var(--deep-green);
    margin-top: 2px;
  }
  .product-title {
    position: absolute;
    left: 100px;
    top: 312px;
    font-family: "Courier Prime", monospace;
    font-weight: 700;
    font-size: 54px;
    line-height: 54px;
    color: var(--deep-green);
  }
  .pet-art {
    position: absolute;
    left: 200px;
    top: 378px;
    width: 210px;
    height: 134px;
    background: linear-gradient(160deg, var(--soft-green), var(--brand-green));
    clip-path: polygon(0 66px, 104px 66px, 104px 0, 210px 0, 210px 134px, 0 134px);
  }
  .rule {
    position: absolute;
    left: 100px;
    width: 305px;
    height: 3px;
    background: var(--brand-green);
  }
  .rule.upper { top: 515px; }
  .rule.lower { top: 571px; }
  .benefits {
    position: absolute;
    left: 100px;
    top: 524px;
    width: 305px;
    font-family: "Raleway", sans-serif;
    font-weight: 300;
    font-size: 27px;
    color: var(--brand-green);
    white-space: nowrap;
  }
  .specs {
    position: absolute;
    left: 100px;
    top: 582px;
    width: 305px;
    display: flex;
    justify-content: space-between;
    font-family: "Raleway", sans-serif;
    font-weight: 600;
    font-size: 16px;
    color: var(--deep-green);
  }
  .flavour {
    position: absolute;
    left: 100px;
    top: 606px;
    font-family: "Courier Prime", monospace;
    font-size: 29px;
    color: var(--deep-green);
    white-space: nowrap;
  }
  .pouch-base {
    position: absolute;
    left: 0;
    bottom: 0;
    width: 440px;
    height: 112px;
    background: linear-gradient(180deg, var(--brand-green), var(--deep-green));
  }
</style>
</head>
<body>
<main class="canvas">
  <section class="pouch">
    <svg class="pouch-top" viewBox="0 0 440 60" aria-hidden="true">
      <path d="M0 0 H440 V14 H300 C270 14 240 22 220 46 C200 22 170 14 140 14 H0 Z" fill="var(--brand-green)"/>
    </svg>

    <div class="line-name">HERBALUXE</div>

    <div class="brand">
      <div class="brand-row">
        <span class="brand-dot"></span>
        <span class="brand-name">VERDALIA</span>
      </div>
      <div class="brand-tag">For Animals</div>
    </div>

    <h1 class="product-title">CBD<br>TREATS</h1>

    <div class="pet-art" role="img" aria-label="Green silhouettes of a sitting cat and dog side by side"></div>

    <div class="rule upper"></div>
    <p class="benefits">SUPPORT | CALM | EASE</p>
    <div class="rule lower"></div>

    <div class="specs">
      <span>120g</span>
      <span>CBD 250mg</span>
      <span>0% THC</span>
    </div>
    <p class="flavour">Chicken Flavour</p>

    <div class="pouch-base" role="img" aria-label="Green base band with a repeating white paw print pattern"></div>
  </section>
</main>
</body>
</html>
```